Innovative Freezer Label Design

Create a versatile and innovative freezer label design with universal appeal, suitable for different functionalities. The design should cater to a diverse audience, including those who freeze meals for meal prepping, batch cooking, and the restaurant industry. Our vision is a visually striking and distinctive design that embodies simplicity.

Example "our current labels feature essential details like "Contents" and "Date." We recognize these as crucial points of information. Currently, the challenge lies in creating various labels for different marketplaces, considering language barriers. A proposed solution involves the integration of universal icons to replace specific words, promoting practicality for international sales."

Kindly note that design concepts should not be restricted to our current product, brand guideline, logo, or the provided example.

Our goal is not only product differentiation but also increased sales through a blend of functionality and aesthetics.

The following are examples of freezer labels designs. Kindly do not restrict your designs to the examples. The designs must be universal (for language barrier purposes)

Examples:
https://www.tackvora.co.uk/pin/5827164039281736401/
https://www.tackvora.co.uk/pin/5827164039281736405/
https://www.tackvora.co.uk/pin/5827164039281736394/
https://www.tackvora.co.uk/pin/5827164039281736308/
https://www.tackvora.co.uk/pin/5827164039281797750/

Please reach out if you have any questions.

Thank you

```html
<!DOCTYPE html>
<html lang="en">
<head>
<meta charset="utf-8">
<title>Freezer Label – Contents</title>
<link rel="stylesheet" href="https://fonts.googleapis.com/css2?family=Cinzel:wght@400&family=Cormorant+Garamond:wght@500&family=Ubuntu:wght@400&display=swap">
<style>
  :root {
    --backdrop: #e5e5e5;
    --label: #ffffff;
    --ink: #333333;
    --ink-light: #ffffff;
  }
  * { box-sizing: border-box; margin: 0; padding: 0; }
  html, body {
    width: 1200px; height: 963px; overflow: hidden;
    background: var(--backdrop);
  }
  .canvas { position: relative; width: 1200px; height: 963px; }
  .label {
    position: absolute; left: 294px; top: 214px; width: 600px; height: 518px;
    background: var(--label);
    border-radius: 174px;
    filter: drop-shadow(7px 8px 5px rgba(0,0,0,0.45));
  }
  .label-frame {
    position: absolute; left: 18px; top: 16px; width: 566px; height: 486px;
    border: 4px solid var(--ink);
    border-radius: 158px;
  }
  .ribbon {
    position: absolute; left: 222px; top: 0; width: 156px; height: 115px;
  }
  .ribbon svg { display: block; width: 100%; height: 100%; }
  .brand-name {
    position: absolute; left: 0; top: 34px; width: 156px; text-align: center;
    font-family: "Cormorant Garamond", serif; font-weight: 500;
    font-size: 19px; letter-spacing: 1.5px; color: var(--ink-light);
  }
  .heading {
    position: absolute; left: 0; top: 138px; width: 600px; text-align: center;
    font-family: "Cinzel", serif; font-weight: 400; font-size: 44px;
    line-height: 1; color: var(--ink);
  }
  .description {
    position: absolute; left: 98px; top: 206px; width: 404px; text-align: center;
    font-family: "Ubuntu", sans-serif; font-size: 12.3px; line-height: 16.8px;
    color: var(--ink);
  }
  .icon-row {
    position: absolute; left: 141px; top: 294px; width: 318px; height: 88px;
    display: flex; justify-content: space-between;
  }
  .icon-badge { width: 88px; height: 88px; }
  .icon-badge svg { display: block; width: 100%; height: 100%; }
  .divider {
    position: absolute; left: 146px; top: 401px; width: 309px; height: 3px;
    background: var(--ink);
  }
  .date {
    position: absolute; left: 0; top: 428px; width: 600px; text-align: center;
    font-family: "Cinzel", serif; font-size: 32px; line-height: 1;
    color: var(--ink);
  }
</style>
</head>
<body>
<main class="canvas">
  <section class="label">
    <div class="label-frame"></div>

    <div class="ribbon">
      <svg viewBox="0 0 156 115" aria-hidden="true">
        <polygon points="0,0 156,0 156,115 78,93 0,115" fill="#333333"/>
      </svg>
      <div class="brand-name">Norvale Keep</div>
    </div>

    <h1 class="heading">Content:</h1>

    <p class="description">Lorem ipsum dolor sit amet, consectetuer adipiscing elit. Quisque arcu ante, cursus in, ornare quis, viverra ut, justo. Quisque vehicula porttitor odio. Donec sit amet enim. Sed a lorem ut est tincidunt consectetuer.</p>

    <div class="icon-row">
      <div class="icon-badge" title="Reusable">
        <svg viewBox="0 0 88 88" aria-hidden="true">
          <circle cx="44" cy="44" r="42.5" fill="none" stroke="#333" stroke-width="1.5" stroke-dasharray="4 3"/>
          <circle cx="44" cy="44" r="19" fill="#333"/>
          <path d="M24 58 A27 27 0 0 1 38 18" fill="none" stroke="#333" stroke-width="3"/>
          <path d="M50 18 A27 27 0 0 1 68 34" fill="none" stroke="#333" stroke-width="3"/>
          <path d="M68 52 A27 27 0 0 1 30 68" fill="none" stroke="#333" stroke-width="3"/>
          <polygon points="64,26 74,26 70,36" fill="#333"/>
          <polygon points="18,58 28,56 24,66" fill="#333"/>
        </svg>
      </div>
      <div class="icon-badge" title="Water and energy saving">
        <svg viewBox="0 0 88 88" aria-hidden="true">
          <circle cx="44" cy="44" r="42.5" fill="none" stroke="#333" stroke-width="1.5" stroke-dasharray="4 3"/>
          <circle cx="44" cy="46" r="22" fill="none" stroke="#333" stroke-width="2"/>
          <circle cx="44" cy="46" r="18" fill="#333"/>
          <path d="M28 14 C22 24 20 28 20 32 A8 8 0 0 0 36 32 C36 28 34 24 28 14 Z" fill="#333" stroke="#fff" stroke-width="1.5"/>
          <polygon points="66,38 56,54 62,54 55,66 70,48 64,48 70,38" fill="#333" stroke="#fff" stroke-width="1.2"/>
        </svg>
      </div>
      <div class="icon-badge" title="Natural">
        <svg viewBox="0 0 88 88" aria-hidden="true">
          <circle cx="44" cy="44" r="42.5" fill="none" stroke="#333" stroke-width="1.5" stroke-dasharray="4 3"/>
          <path d="M50 14 C64 26 66 46 58 58 C52 66 42 66 36 60 C30 54 36 42 44 36 C50 30 50 22 50 14 Z" fill="#333"/>
          <path d="M50 16 C56 30 56 46 38 64 L24 66" fill="none" stroke="#fff" stroke-width="1.2"/>
          <path d="M26 64 L38 62" fill="none" stroke="#333" stroke-width="2.5"/>
        </svg>
      </div>
    </div>

    <div class="divider"></div>

    <p class="date">04.12.2023</p>
  </section>
</main>
</body>
</html>
```